Stunning Podcast Cover Design for The Morning Brook Hour!!

I need a design for my new podcast.
I will need it in a variety of size/formats, such as a large version for my podcast website homepage, the thumbnail for TuneVault, Loomcast, Pindle Store and more.

The podcast is called "The Morning Brook Hour" and it includes topics such as: business, entrepreneurship, finance, budgeting, estate planning, end-of-life planning, travel, business and personal stories featuring people from all over the world, life in general, and more.

I don't have a vision in mind so am looking for creativity but it definitely needs to have the colour gold in it somewhere! No cartoon characters please.

I will provide comments/feedback to each designer.

***UPDATE: Please see some photos of me that can be used in the podcast design.

Here is some tips on creating podcast designs. https://www.wavernest.com/blog/10-tips-create-awesome-podcast-artwork

Target Market(s)

Adults 25 - 65

Font styles to use
Other font styles liked:
• something modern - see my company logo as an example

Colors

Designer to choose colors to be used in the design.

Requirements
Must have
• The colour gold in it
Nice to have
• I feel like the word "The" should be smaller then the other three words.
• I would like to see designs with a white coloured background and a black coloured one also...
• Perhaps designs with a filter over the photo, and without.
• Perhaps use my photo, or don't use my photo!
• Please see some photos of me that can be used in the podcast design.
• Here is some tips on creating podcast designs. https://www.wavernest.com/blog/10-tips-create-awesome-podcast-artwork
Should not have
• cartoon characters
• Corny 1990's "Evenings with the Grand and Glittering" look - see https://www.clipharbor.com/watch?v=Q7T2KX8PLWZ

```html
<!DOCTYPE html>
<html lang="en">
<head>
<meta charset="utf-8">
<title>The Morning Brook Hour — Podcast Cover</title>
<link rel="stylesheet" href="https://fonts.googleapis.com/css2?family=Oswald:wght@500;600&display=swap">
<style>
  :root {
    --ink-deep: #050505;
    --ink-core: #252525;
    --gold-dark: #9a5f18;
    --gold-mid: #c98a2b;
    --gold-warm: #f2c04c;
    --gold-light: #fff3b0;
    --gold-gradient: linear-gradient(90deg,
      var(--gold-warm) 0%, var(--gold-mid) 12%, var(--gold-dark) 22%,
      var(--gold-warm) 34%, var(--gold-light) 46%, var(--gold-warm) 58%,
      var(--gold-dark) 70%, var(--gold-mid) 84%, var(--gold-warm) 100%);
  }
  * { margin: 0; padding: 0; box-sizing: border-box; }
  html, body {
    width: 1200px; height: 1200px; overflow: hidden;
    background: var(--ink-deep);
  }
  .cover {
    position: relative;
    width: 1200px; height: 1200px;
    background: radial-gradient(circle at 50% 50%, var(--ink-core) 0%, #141414 45%, var(--ink-deep) 100%);
  }
  .cover__frame {
    position: absolute;
    left: 34px; top: 34px;
    width: 1132px; height: 1132px;
    border: 17px solid transparent;
    border-image: var(--gold-gradient) 1;
  }
  .cover__title {
    position: absolute;
    inset: 0;
    display: flex;
    flex-direction: column;
    align-items: center;
    justify-content: center;
    padding-bottom: 10px;
    font-family: "Oswald", "Arial Narrow", sans-serif;
    text-transform: uppercase;
    text-align: center;
  }
  .cover__line {
    display: block;
    background: var(--gold-gradient);
    -webkit-background-clip: text;
    background-clip: text;
    color: transparent;
  }
  .cover__line--small {
    font-size: 84px;
    font-weight: 600;
    line-height: 100px;
    letter-spacing: 2px;
    margin-bottom: 8px;
  }
  .cover__line--large {
    font-size: 238px;
    font-weight: 500;
    line-height: 268px;
    letter-spacing: -2px;
  }
</style>
</head>
<body>
  <main class="cover">
    <div class="cover__frame"></div>
    <h1 class="cover__title">
      <span class="cover__line cover__line--small">The</span>
      <span class="cover__line cover__line--large">Morning</span>
      <span class="cover__line cover__line--large">Brook</span>
      <span class="cover__line cover__line--large">Hour</span>
    </h1>
  </main>
</body>
</html>
```